Awesome business card design needed

We need a new business card design to go with our new logo.
We are a web development agency that specialises in highly complex back-end integrations as opposed to design, our customers are retailers, hotels, hospitals and any other organisation that has a large online marketing department.
Take a look at our website - www.orvekplus.com for some inspiration.
We want our new business cards to exude class, professionalism and style.
We are likely to choose a high-end card to print them on but we want the design of the card itself to really turn heads.
We have no specific colour requirements, the logo as you will see is a turquoise colour R89 G171 B167 #59aba7 but it can also be in white if you want to make the colour of the card something different.
The information on the card should be:
Name
Position
Tel
email
Potentially a double sided card could have our web address, twitter and FB links.

```html
<!DOCTYPE html>
<html lang="en">
<head>
<meta charset="utf-8">
<title>OrvekPlus Business Card</title>
<link rel="stylesheet" href="https://fonts.googleapis.com/css2?family=Cinzel:wght@400;700&display=swap">
<style>
  :root {
    --page-bg: #e9ebea;
    --card-dark: #1c1f21;
    --card-dark-2: #2a2e31;
    --teal: #59aba7;
    --teal-light: #9fdcd8;
    --teal-pale: #bfe6e3;
    --ink-dark: #14191a;
    --white: #ffffff;
  }
  html, body {
    margin: 0;
    width: 1200px;
    height: 1200px;
    overflow: hidden;
    background: var(--page-bg);
    font-family: "Cinzel", serif;
  }
  .canvas {
    width: 1200px;
    height: 1200px;
    display: flex;
    flex-direction: column;
    align-items: center;
    justify-content: center;
    gap: 70px;
  }
  .card {
    position: relative;
    width: 840px;
    height: 480px;
    box-sizing: border-box;
    box-shadow: 0 10px 30px rgba(0,0,0,0.25);
  }

  /* Front */
  .card-front {
    background: linear-gradient(160deg, var(--card-dark-2), var(--card-dark) 70%);
  }
  .front-brand {
    position: absolute;
    top: 120px;
    left: 0;
    right: 0;
    text-align: center;
  }
  .brand-name {
    font-weight: 700;
    color: var(--teal-light);
    font-size: 78px;
    letter-spacing: 2px;
    line-height: 1;
    margin: 0;
    text-transform: lowercase;
  }
  .brand-sub {
    margin: 8px 0 0 250px;
    color: var(--white);
    font-size: 20px;
    letter-spacing: 1px;
    text-align: left;
  }
  .front-band {
    position: absolute;
    left: 0;
    right: 0;
    bottom: 50px;
    height: 34px;
    background: var(--teal);
    display: flex;
    align-items: center;
    justify-content: center;
    color: var(--white);
    font-size: 14px;
    font-weight: 700;
    letter-spacing: 1px;
  }
  .front-band::after {
    content: "";
    position: absolute;
    left: 0; right: 0;
    bottom: -10px;
    height: 3px;
    background: var(--teal);
  }

  /* Back */
  .card-back {
    background: linear-gradient(180deg, var(--teal-pale) 0%, var(--teal) 45%, #2a4a49 85%, #1b2526 100%);
    padding: 40px 50px;
    color: var(--ink-dark);
  }
  .person-name {
    margin: 0;
    font-size: 30px;
    font-weight: 400;
    letter-spacing: 1px;
  }
  .person-role {
    margin: 4px 0 0;
    font-size: 24px;
    letter-spacing: 1px;
  }
  .contact-list {
    list-style: none;
    margin: 38px 0 0;
    padding: 0;
    font-size: 14px;
    font-weight: 700;
    line-height: 1.8;
  }
  .contact-list .label { margin-right: 8px; }
  .social-list {
    position: absolute;
    left: 50px;
    bottom: 50px;
    list-style: none;
    margin: 0;
    padding: 0;
    font-size: 14px;
    font-weight: 700;
    line-height: 2;
    color: var(--teal-light);
  }
  .back-brand {
    position: absolute;
    right: 60px;
    bottom: 60px;
    text-align: right;
  }
  .back-brand .brand-name { font-size: 72px; }
  .back-brand .brand-sub {
    margin: 6px 0 0;
    text-align: right;
    font-size: 20px;
  }
</style>
</head>
<body>
<main class="canvas">
  <section class="card card-front" aria-label="Card front">
    <div class="front-brand">
      <p class="brand-name">orvekplus</p>
      <p class="brand-sub">OrvekPlus, Ltd</p>
    </div>
    <div class="front-band">www.orvekplus.com</div>
  </section>

  <section class="card card-back" aria-label="Card back">
    <h1 class="person-name">Mara Ellison</h1>
    <p class="person-role">Co-Founder</p>
    <ul class="contact-list">
      <li><span class="label">CONTACT:</span>01632 555870</li>
      <li><span class="label">EMAIL:</span>info@orvekplus.com</li>
      <li><span class="label">WEB:</span>www.orvekplus.com</li>
    </ul>
    <ul class="social-list">
      <li>www.chirpline.com/orvekplus</li>
      <li>www.friendspage.com/OrvekPlus</li>
    </ul>
    <div class="back-brand">
      <p class="brand-name">orvekplus</p>
      <p class="brand-sub">OrvekPlus, Ltd</p>
    </div>
  </section>
</main>
</body>
</html>
```